Offshore Energy Projects Management Consultancy needs a business card design

Logo available. We provide teams to deliver engineering consultancy, project management and delivery teams mainly in the offshore renewables sector. The company is all about bringing the right people to a project to deliver the scope.

The business card will be used for all staff.

The business card should be quite simple, vibrant and uncluttered but convey experience, enthusiasm and integration.

Target Market(s)

Energy Project Developers and Tier 1 construction companies

Contact Information for Business Card

Logo should be on the back of the card. I'm happy for the designer to play with the colour of the logo and background colour.

Front of the card should convey all the must have information in a clear and professional manner but without being overly traditional.

Colors

Designer to choose colors to be used in the design.

Requirements
Must have
• Land Line Tel Number, Mobile Tel Number, Email, business address, web address.

```html
<!DOCTYPE html>
<html lang="en">
<head>
<meta charset="utf-8">
<title>Tidewater Delivery Group – Business Card</title>
<link rel="stylesheet" href="https://fonts.googleapis.com/css2?family=Ubuntu:wght@400;500;700&display=swap">
<style>
  :root {
    --page-bg: #e6e3de;
    --brand-blue: #1168b1;
    --brand-blue-light: #2a9fe0;
    --slate: #656a70;
    --ink: #3a3d42;
    --card-white: #f4f4f3;
    --white: #ffffff;
  }
  * { margin: 0; padding: 0; box-sizing: border-box; }
  html, body {
    width: 900px; height: 1200px; overflow: hidden;
    background: var(--page-bg);
    font-family: "Ubuntu", Arial, sans-serif;
  }
  .canvas { position: relative; width: 900px; height: 1200px; }

  .card {
    position: absolute;
    border-radius: 22px;
    overflow: hidden;
  }

  /* Back of card */
  .card-back {
    left: 78px; top: 135px; width: 762px; height: 435px;
    background: var(--brand-blue);
  }
  .card-back .pattern-field {
    position: absolute; inset: 0;
    background: linear-gradient(135deg, #1570b8 0%, var(--brand-blue) 55%, #0f61a6 100%);
  }
  .card-back .wordmark {
    position: absolute; left: 390px; top: 222px;
    color: var(--white);
    font-size: 50px; font-weight: 500; letter-spacing: 1px;
  }

  /* Front of card */
  .card-front {
    left: 76px; top: 630px; width: 767px; height: 435px;
    background: var(--card-white);
  }
  .card-front .panels { position: absolute; inset: 0; }

  .brand-lockup {
    position: absolute; left: 42px; top: 62px; width: 300px;
    display: flex; align-items: center; gap: 12px;
  }
  .brand-lockup .brand-square {
    width: 22px; height: 22px; background: var(--brand-blue); flex: none;
  }
  .brand-lockup .brand-name {
    color: var(--slate); font-size: 25px; font-weight: 500; line-height: 1.15;
    text-transform: uppercase;
  }

  .contact-list {
    position: absolute; left: 34px; list-style: none;
    color: var(--ink); font-size: 19px;
  }
  .contact-list li { display: flex; align-items: center; gap: 14px; height: 29px; }
  .contact-list svg { width: 24px; height: 24px; flex: none; }
  .contact-list.phones { top: 257px; }
  .contact-list.online { top: 342px; }
  .contact-list .web { font-weight: 500; }

  .person {
    position: absolute; right: 42px; top: 74px; text-align: right; color: var(--white);
  }
  .person .name { font-size: 26px; font-weight: 500; letter-spacing: 0.5px; }
  .person .role { font-size: 21px; font-weight: 400; margin-top: 2px; }

  .address {
    position: absolute; right: 46px; top: 345px; text-align: right;
    color: var(--white); font-size: 19px; line-height: 1.35;
  }
</style>
</head>
<body>
<main class="canvas">

  <section class="card card-back" aria-label="Card back">
    <div class="pattern-field" role="img" aria-label="Repeating brand monogram pattern in light blue on blue"></div>
    <div class="wordmark">TIDEWATER</div>
  </section>

  <section class="card card-front" aria-label="Card front">
    <svg class="panels" width="767" height="435" viewBox="0 0 767 435" aria-hidden="true">
      <polygon points="284,0 767,0 767,213 388,213" fill="var(--brand-blue)"/>
      <polygon points="391,220 767,220 767,435 497,435" fill="var(--slate)"/>
    </svg>

    <div class="brand-lockup">
      <span class="brand-square"></span>
      <span class="brand-name">Tidewater<br>Delivery Group</span>
    </div>

    <div class="person">
      <div class="name">MARCUS HALE</div>
      <div class="role">owner</div>
    </div>

    <ul class="contact-list phones">
      <li>
        <svg viewBox="0 0 24 24" aria-hidden="true"><path fill="var(--brand-blue)" d="M3 8c0-2 4-4 9-4s9 2 9 4v2h-5V8c-1-.6-2.4-1-4-1s-3 .4-4 1v2H3zM6 11h12l2 8H4z"/><circle cx="12" cy="15" r="2.3" fill="var(--card-white)"/></svg>
        020 555 0142
      </li>
      <li>
        <svg viewBox="0 0 24 24" aria-hidden="true"><rect x="6" y="2" width="12" height="20" rx="2" fill="none" stroke="var(--brand-blue)" stroke-width="2"/><circle cx="12" cy="18.5" r="1.2" fill="var(--brand-blue)"/></svg>
        070 555 0187
      </li>
    </ul>

    <ul class="contact-list online">
      <li>
        <svg viewBox="0 0 24 24" aria-hidden="true"><rect x="2" y="5" width="20" height="14" fill="var(--brand-blue)"/><path d="M2 6l10 7 10-7" fill="none" stroke="var(--card-white)" stroke-width="1.6"/></svg>
        hello@tidewaterdelivery.com
      </li>
      <li>
        <svg viewBox="0 0 24 24" aria-hidden="true"><g fill="none" stroke="var(--brand-blue)" stroke-width="1.8"><circle cx="12" cy="12" r="9"/><ellipse cx="12" cy="12" rx="4" ry="9"/><path d="M3 12h18M5 7h14M5 17h14"/></g></svg>
        <span class="web">www.tidewaterdelivery.com</span>
      </li>
    </ul>

    <div class="address">27 Harbourline Road<br>Seabrook, NJ 08302</div>
  </section>

</main>
</body>
</html>
```